Web Design For Metal Recycling Company

We are a scrap and recycling company dealing mainly in scrap metal base in Singapore. We deal in both domestic market and international market. Currently we are still unsure if we want to have a "lively" or "professional" company image so we will leave it to the designer to deem what is good.

We wish for a website to be able to "Retain" the interest of new visitor and at the same time able to give enough information for new and existing customer. We would also wish for design that will get the visitor to "Engage" us.

The attached is the logo for the company and we would want to incorporate that into the website. Either of the logo is fine.

```html
<!DOCTYPE html>
<html lang="en">
<head>
<meta charset="utf-8">
<title>Kim Lian Hock Recycling</title>
<link href="https://fonts.googleapis.com/css2?family=Ubuntu:ital,wght@0,300;0,400;0,500;0,700;1,400&display=swap" rel="stylesheet">
<style>
:root{
  --gold:#d9a53a;
  --gold-light:#f1c766;
  --gold-dark:#8a5f12;
  --ink:#1b1b1b;
  --charcoal:#353535;
  --paper:#f4f4f4;
  --text:#555;
  --muted:#777;
  --white:#fff;
}
*{box-sizing:border-box;margin:0;padding:0}
html,body{width:991px;height:1200px;overflow:hidden}
body{position:relative;font-family:"Ubuntu",sans-serif;background:var(--paper);color:var(--text)}
.abs{position:absolute}

/* header */
.topline{left:0;top:0;width:991px;height:6px;background:linear-gradient(90deg,#b8861f,#f1c766,#b8861f)}
.header{left:0;top:6px;width:991px;height:116px;background:linear-gradient(180deg,#2a2a2a,#111);border-bottom:1px solid #3a3a6a}
.brand{left:118px;top:40px;display:flex;align-items:center;gap:10px;color:var(--gold);font-weight:700;font-size:19px;line-height:1.1;letter-spacing:.5px;text-transform:uppercase}
.brand-mark{width:40px;height:40px;border:3px solid var(--gold)}
.contact-top{top:38px;color:var(--white);font-size:13px;display:flex;align-items:center;gap:6px}
.contact-top.phone{font-size:16px}
.nav{left:373px;top:73px;height:28px;display:flex;background:linear-gradient(180deg,var(--gold-light),var(--gold));box-shadow:0 1px 3px rgba(0,0,0,.5)}
.nav a{display:block;padding:0 8px;line-height:28px;font-size:11px;color:#2a1c05;text-decoration:none;border-right:1px solid #a97a20}
.nav a:last-child{border-right:0}
.nav a.active{background:linear-gradient(180deg,#e8e8e8,#a9a9a9);width:64px;text-align:center;color:#333}

/* hero */
.hero{left:0;top:122px;width:991px;height:368px;background:linear-gradient(110deg,#6b655e 0%,#4b4743 30%,#bfb9b0 55%,#8f8a84 75%,#c8563c 100%)}
.hero-caption{left:117px;top:344px;width:351px;height:98px;background:rgba(20,20,20,.82);color:var(--white);font-style:italic;font-size:23px;line-height:1.3;padding:20px 12px}
.dots{left:455px;top:467px;display:flex;gap:5px}
.dots span{width:12px;height:12px;border-radius:50%;background:var(--white)}
.dots span:first-child{background:var(--gold)}

/* intro */
.sq{display:inline-block;width:18px;height:18px;border:2px solid var(--gold);vertical-align:middle;margin-right:6px}
.welcome{left:110px;top:512px;font-size:14px;color:#444;font-weight:500}
.welcome b{color:var(--gold);font-weight:700;text-transform:uppercase}
.intro-text{left:110px;top:544px;width:520px;font-size:10px;line-height:14px;color:var(--muted)}
.dash{left:108px;top:595px;width:521px;border-top:1px dashed #999}
.deal-title{left:110px;top:604px;font-size:14px;color:#444;font-weight:500}
.deal{width:175px;font-size:12px;color:#444;text-transform:uppercase}
.deal svg{vertical-align:-2px;margin-right:3px}
.deal p{text-transform:none;font-size:10px;line-height:14px;color:var(--muted);margin:4px 0 0 16px}

/* form */
.help{left:643px;top:514px;width:232px;height:222px;background:var(--white);border:1px solid #ddd;box-shadow:0 3px 4px rgba(0,0,0,.15);padding:12px 15px}
.help h3{font-weight:400;font-size:14px;color:#444;padding-bottom:8px;border-bottom:1px solid #e2e2e2;margin-bottom:8px}
.field{height:21px;border:1px solid #ccc;border-radius:2px;margin-bottom:8px;font-size:10px;color:#999;padding:4px 7px}
.field.msg{height:52px}
.btn{display:inline-block;background:linear-gradient(180deg,var(--gold-light),#c08c2a);color:#2a1c05;font-size:10px;font-weight:700;padding:5px 11px;border-radius:2px}

/* services */
.services{left:0;top:763px;width:991px;height:262px;background:var(--charcoal);border-top:1px solid #ccc}
.svc-title{left:168px;top:16px;width:655px;display:flex;align-items:center;gap:8px;color:var(--white);font-size:23px;font-weight:300;white-space:nowrap}
.svc-title i{flex:1;height:4px;border-top:1px solid #ccc;border-bottom:1px solid #ccc}
.svc{width:190px;text-align:center;top:60px}
.svc h4{color:var(--gold);font-weight:500;font-size:13px;text-transform:uppercase;height:30px}
.circle{width:84px;height:84px;margin:12px auto 18px;border-radius:50%;background:var(--white);border:3px solid var(--gold);display:flex;align-items:center;justify-content:center}
.svc p{color:var(--white);font-size:10px;line-height:14px}
.divider{top:70px;width:1px;height:150px;background:#2a2a2a;border-right:1px solid #444}
.arrow{top:118px}

/* footer */
.footer{left:0;top:1025px;width:991px;height:157px;background:linear-gradient(180deg,#8f6512,#c49433)}
.footer h5{color:var(--white);font-weight:500;font-size:13px}
.links{list-style:none;margin-top:12px}
.links li{color:var(--white);font-size:11px;line-height:17.6px;padding-left:15px;position:relative}
.links li:before{content:"";position:absolute;left:3px;top:7px;border:2px solid transparent;border-left:3px solid var(--white)}
.nl p{color:var(--white);font-size:11px;line-height:19px;margin-top:10px}
.email-in{width:151px;height:25px;background:var(--white);border:1px solid #ddd;font-size:11px;color:#333;padding:5px 7px;margin-top:8px}
.sub{display:inline-block;background:linear-gradient(180deg,#f4f4f4,#bdbdbd);color:#222;font-size:10px;padding:3px 8px;margin-top:13px;border-radius:2px}
.map{left:432px;top:1063px;width:140px;height:100px;border:3px solid var(--white);background:linear-gradient(135deg,#efe4c6,#e8d08a 50%,#b5c9e3)}
.ci{left:590px;display:flex;gap:10px;color:var(--white);font-size:11px;line-height:14px;width:170px}
.ci svg{flex:none}
.foot-mark{left:802px;top:1065px;width:57px;height:55px;border:3px solid #2a2a2a}
.socials{left:772px;top:1142px;display:flex;gap:18px}
.socials span{width:16px;height:16px;border-radius:50%;background:var(--white)}
.copyright{left:0;top:1182px;width:991px;height:18px;background:#5a4313;color:var(--white);font-size:10px;text-align:center;line-height:18px}
</style>
</head>
<body>
<div class="abs topline"></div>
<header class="abs header"></header>
<div class="abs brand"><span class="brand-mark"></span><span>Kim Lian Hock<br>Recycling</span></div>
<div class="abs contact-top" style="left:590px">
  <svg width="16" height="11" viewBox="0 0 16 11"><rect x=".5" y=".5" width="15" height="10" fill="none" stroke="#d9a53a"/><path d="M.5 .5 8 6l7.5-5.5" fill="none" stroke="#d9a53a"/></svg>info@kimlianhock.com</div>
<div class="abs contact-top phone" style="left:762px">
  <svg width="16" height="16" viewBox="0 0 16 16"><circle cx="8" cy="8" r="7" fill="none" stroke="#d9a53a" stroke-width="1.5"/><path d="M6 4l1.5 3-1 1 2 2.5 1-1 2 1.5" fill="none" stroke="#d9a53a" stroke-width="1.3"/></svg>0100 200 300</div>
<nav class="abs nav">
  <a class="active">Home</a><a>Product &amp; Services</a><a>Health &amp; Safety</a><a>Resources</a><a>About</a><a>Location</a><a>Contact Us</a>
</nav>

<div class="abs hero" role="img" aria-label="Scrap yard with a grab crane lifting mixed scrap metal beside a material handler"></div>
<div class="abs hero-caption">We deal in both Domestic market and International market.</div>
<div class="abs dots"><span></span><span></span><span></span><span></span><span></span></div>

<div class="abs welcome"><span class="sq"></span>Welcome to <b>Kim Lian Hock Recycling</b></div>
<p class="abs intro-text">Lorem ipsum dolor sit amet, consectetuer adipiscing elit, sed diam nonummy nibh euismod tincidunt ut laoreet dolore magna aliquam erat volutpat. Lorem ipsum dolor sit amet, consectetuer adipiscing elit, sed diam nonummy nibh euismod tincidunt ut laoreet dolore magna aliquam erat volutpat.</p>
<div class="abs dash"></div>
<div class="abs deal-title"><span class="sq"></span>We Deal In:</div>

<div class="abs deal" style="left:112px;top:634px"><svg width="14" height="12" viewBox="0 0 14 12"><path d="M1 6l4 4 8-9" fill="none" stroke="#d9a53a" stroke-width="2.5"/></svg>Process<p>Duis autem vel eum iriure dolor in hendrerit in</p></div>
<div class="abs deal" style="left:292px;top:634px"><svg width="14" height="12" viewBox="0 0 14 12"><path d="M1 6l4 4 8-9" fill="none" stroke="#d9a53a" stroke-width="2.5"/></svg>Ferrous<p>Duis autem vel eum iriure dolor in hendrerit in</p></div>
<div class="abs deal" style="left:478px;top:634px"><svg width="14" height="12" viewBox="0 0 14 12"><path d="M1 6l4 4 8-9" fill="none" stroke="#d9a53a" stroke-width="2.5"/></svg>Non-Ferrous<p>Duis autem vel eum iriure dolor in hendrerit in</p></div>
<div class="abs deal" style="left:112px;top:695px"><svg width="14" height="12" viewBox="0 0 14 12"><path d="M1 6l4 4 8-9" fill="none" stroke="#d9a53a" stroke-width="2.5"/></svg>Electronics<p>Duis autem vel eum iriure dolor in hendrerit in</p></div>
<div class="abs deal" style="left:292px;top:695px"><svg width="14" height="12" viewBox="0 0 14 12"><path d="M1 6l4 4 8-9" fill="none" stroke="#d9a53a" stroke-width="2.5"/></svg>Machinery<p>Duis autem vel eum iriure dolor in hendrerit in</p></div>
<div class="abs deal" style="left:478px;top:695px"><svg width="14" height="12" viewBox="0 0 14 12"><path d="M1 6l4 4 8-9" fill="none" stroke="#d9a53a" stroke-width="2.5"/></svg>Others<p>Duis autem vel eum iriure dolor in hendrerit in</p></div>

<form class="abs help">
  <h3><span class="sq"></span>How&nbsp; can we help you?</h3>
  <div class="field">Name</div>
  <div class="field">Email</div>
  <div class="field">Phone</div>
  <div class="field msg">Message</div>
  <span class="btn">SUBMIT</span>
</form>

<section class="abs services">
  <div class="abs svc-title"><i></i>Product &amp; Services<i></i></div>
  <svg class="abs arrow" style="left:117px" width="20" height="26" viewBox="0 0 20 26"><path d="M16 2 5 13l11 11" fill="none" stroke="#888" stroke-width="4"/></svg>
  <svg class="abs arrow" style="left:854px" width="20" height="26" viewBox="0 0 20 26"><path d="M4 2l11 11L4 24" fill="none" stroke="#888" stroke-width="4"/></svg>
  <div class="abs svc" style="left:118px"><h4>Buying</h4><div class="circle"><svg width="46" height="46" viewBox="0 0 46 46"><circle cx="23" cy="12" r="9" fill="none" stroke="#333" stroke-width="2.5"/><circle cx="13" cy="26" r="4" fill="#333"/><circle cx="33" cy="26" r="4" fill="#333"/><path d="M5 44v-8a8 8 0 0 1 16 0v8zM25 44v-8a8 8 0 0 1 16 0v8z" fill="#333"/></svg></div><p>Lorem ipsum dolor sit,<br>consectetuedipiscing elit, sed</p></div>
  <div class="abs divider" style="left:312px"></div>
  <div class="abs svc" style="left:306px"><h4>Selling</h4><div class="circle"><svg width="46" height="46" viewBox="0 0 46 46"><rect x="12" y="4" width="22" height="20" rx="2" fill="#333"/><path d="M3 28c8 0 12 3 18 3h10c3 0 3 4 0 4H21l11 1 10-6c3-2 5 1 2 3L30 42H14L3 38z" fill="#333"/></svg></div><p>Lorem ipsum dolor sit,<br>consectetuedipiscing elit, sed</p></div>
  <div class="abs divider" style="left:498px"></div>
  <div class="abs svc" style="left:495px"><h4>Scrap Managment</h4><div class="circle"><svg width="50" height="46" viewBox="0 0 50 46"><circle cx="25" cy="9" r="6" fill="#333"/><path d="M17 28v-6a8 8 0 0 1 16 0v6z" fill="#333"/><path d="M6 27l10 4h18l10-4M25 31v8" stroke="#333" stroke-width="2"/><circle cx="5" cy="27" r="4" fill="#333"/><circle cx="45" cy="27" r="4" fill="#333"/><circle cx="25" cy="41" r="4" fill="#333"/></svg></div><p>Lorem ipsum dolor sit,<br>consectetuedipiscing elit, sed</p></div>
  <div class="abs divider" style="left:690px"></div>
  <div class="abs svc" style="left:684px"><h4>Recycling</h4><div class="circle"><svg width="46" height="46" viewBox="0 0 46 46"><path d="M16 6h14l6 10-6 3-7-11zM38 22l7 12-7 10-5-6 5-9zM30 42H16l-7-11 6-3 6 10h9zM8 30 1 18 9 8l3 7-4 8z" fill="#333"/></svg></div><p>Lorem ipsum dolor sit,<br>consectetuedipiscing elit, sed</p></div>
</section>

<footer class="abs footer"></footer>
<div class="abs" style="left:118px;top:1034px"><h5>Quick Links</h5>
  <ul class="links"><li>Home</li><li>Product &amp; Services</li><li>Health &amp; Safety</li><li>Resources</li><li>About</li><li>Location</li><li>Contact Us</li></ul></div>
<div class="abs nl" style="left:254px;top:1034px"><h5>Subscribe for Newsletter</h5><p>Get the latest updates by<br>entering your email address</p><div class="email-in">Enter your email</div><span class="sub">SUBSCRIBE</span></div>
<div class="abs" style="left:432px;top:1034px"><h5>Contact Info</h5></div>
<div class="abs map" role="img" aria-label="Street map showing the company location"></div>
<div class="abs ci" style="top:1061px"><svg width="12" height="16" viewBox="0 0 12 16"><path d="M6 0a6 6 0 0 1 6 6c0 4-6 10-6 10S0 10 0 6a6 6 0 0 1 6-6z" fill="#fff"/><circle cx="6" cy="6" r="2" fill="#b88a2c"/></svg><span>Duis autem vel eum iriure<br>dolor in hendrerit in</span></div>
<div class="abs ci" style="top:1098px"><svg width="12" height="12" viewBox="0 0 12 12"><path d="M2 0l3 3-1.5 2L7 8.5 9 7l3 3-2 2C5 12 0 7 0 2z" fill="#fff"/></svg><span>0100 200 300</span></div>
<div class="abs ci" style="top:1122px"><svg width="14" height="11" viewBox="0 0 14 11"><rect width="14" height="11" fill="#fff"/><path d="M0 0l7 6 7-6" fill="none" stroke="#b88a2c"/></svg><span>info@kimlianhock.com</span></div>
<div class="abs ci" style="top:1147px"><svg width="14" height="12" viewBox="0 0 14 12"><rect x="3" y="0" width="8" height="4" fill="#fff"/><rect x="0" y="4" width="14" height="5" rx="1" fill="#fff"/><rect x="3" y="8" width="8" height="4" fill="#fff"/></svg><span>0100 200 300</span></div>
<div class="abs foot-mark"></div>
<div class="abs socials"><span></span><span></span><span></span><span></span></div>
<div class="abs copyright">© 2014 Kimlianhock. All right reserved.</div>
</body>
</html>
```